3D printers services needs a brochure

We need a Creative, Innovative idea for a brochure. 3d printing for Prototyping, .
We would like to have an A4 horizontal brochure that could give a 3D effect when folded or cut.
Our name is K7! Gather! Shape! Go! our website is www.k7venturelab.example. Please be inspired by our logo and the dreamy cloud part.
Our prospects: Architects, Artists, Museums and Designers ( Jewellery, watches, etc ...)
What we offer:
.3D printing and prototyping.
.3D scanning.
.Transforming 2D images to 3D objects.
. Making their Portals where clients can visualize, personalize (IN 3D) and order their work.

Reason: I would like to extend it because i figured out the deadline is too short! Thank you Best regards Tarek

```html
<!DOCTYPE html>
<html lang="en">
<head>
<meta charset="utf-8">
<title>K7 Venture Lab – Trifold Brochure</title>
<link rel="stylesheet" href="https://fonts.googleapis.com/css2?family=Lato:ital,wght@0,400;0,700;1,400&family=Ultra&display=swap">
<style>
  :root{
    --stage:#3a3a3a;
    --blue:#0b55c9;
    --blue-deep:#062c80;
    --blue-night:#041c55;
    --lime:#c6dc1f;
    --ink:#0a0a0a;
    --white:#ffffff;
    --grey-text:#4a4a4a;
    --sky:#7fb4cf;
    --dusk:#d98a45;
    --brick:#6a2f1c;
  }
  *{margin:0;padding:0;box-sizing:border-box}
  html,body{width:1200px;height:801px;overflow:hidden;background:var(--stage)}
  body{font-family:"Lato",Arial,sans-serif;color:var(--white)}

  .brochure{position:absolute;left:60px;top:18px;width:1080px;height:765px;display:flex;box-shadow:0 6px 24px rgba(0,0,0,.5)}
  .panel{position:relative;width:360px;height:765px;overflow:hidden}

  /* About panel */
  .panel--about{background:linear-gradient(135deg,var(--blue) 0%,var(--blue-deep) 70%,var(--blue-night) 100%)}
  .about__visual{position:absolute;left:22px;top:26px;width:300px;height:200px}
  .about__heading{position:absolute;left:0;top:244px;width:360px;height:42px;background:linear-gradient(90deg,#0a0a0a 0%,#0a0a0a 55%,rgba(10,10,10,0) 100%);padding-left:22px;display:flex;align-items:center}
  .about__heading h2{font-family:"Ultra",Georgia,serif;font-weight:400;font-size:26px;letter-spacing:1px;color:var(--lime)}
  .about__body{position:absolute;left:22px;right:22px;top:296px}
  .about__lead{font-weight:700;font-size:18px;margin-bottom:6px}
  .about__body p{font-size:11.2px;line-height:1.3;text-align:justify;margin-bottom:9px}

  /* Contact panel */
  .panel--contact{background:radial-gradient(ellipse at 50% 45%,#3a3a3a 0%,#161616 45%,var(--ink) 80%)}
  .brandmark{position:absolute;left:0;right:0;top:335px;text-align:center}
  .brandmark__name{font-weight:700;font-size:46px;line-height:1;letter-spacing:2px}
  .brandmark__tag{font-weight:700;font-size:12px;letter-spacing:1px;margin-top:16px}
  .panel--contact .brandmark__name,.panel--contact .brandmark__tag{color:var(--white)}
  .contact-list{position:absolute;left:0;right:0;top:474px;list-style:none;text-align:center}
  .contact-list li{font-style:italic;font-size:15px;height:32px;display:flex;align-items:center;justify-content:center;gap:8px}
  .contact-list li.contact--address{font-size:12.5px}
  .contact-list svg{flex:none}
  .social{position:absolute;left:0;right:0;top:663px;display:flex;justify-content:center;gap:12px}
  .social span{width:24px;height:24px;border-radius:50%}
  .social .s1{background:#3b5ba0}.social .s2{background:#29a9e1}.social .s3{background:#1e88b4}.social .s4{background:#f39b1e}
  .web-band{position:absolute;left:0;right:0;top:710px;height:32px;display:flex;align-items:center;justify-content:center;font-weight:700;font-size:15px;letter-spacing:3px;color:var(--lime)}
  .panel--contact .web-band{background:var(--blue-night)}
  .panel--contact .web-tail{position:absolute;left:0;right:0;top:742px;bottom:0;background:var(--blue-deep)}

  /* Cover panel */
  .panel--cover{background:linear-gradient(180deg,var(--blue) 0%,var(--blue-deep) 100%)}
  .cover__photo{position:absolute;left:0;top:0;width:360px;height:547px;background:linear-gradient(180deg,var(--sky) 0%,#a9c4c4 28%,var(--dusk) 48%,var(--brick) 62%,#3d2418 100%)}
  .cover__rule{position:absolute;left:0;right:0;top:547px;height:5px;background:var(--lime)}
  .cover__rule::after{content:"";position:absolute;left:0;right:0;top:5px;height:2px;background:var(--white)}
  .cover__plate{position:absolute;left:65px;top:445px;width:230px;height:138px;border-radius:50%;background:var(--white);box-shadow:0 4px 10px rgba(0,0,0,.35);display:flex;flex-direction:column;align-items:center;justify-content:center}
  .cover__plate .brandmark__name,.cover__plate .brandmark__tag{color:var(--grey-text)}
  .cover__plate .brandmark__name{font-size:38px}
  .cover__plate .brandmark__tag{font-size:10px;margin-top:10px}
  .cover__title{position:absolute;left:0;right:0;top:605px;text-align:center;font-family:"Ultra",Georgia,serif;font-weight:400;font-size:31px;letter-spacing:1px;color:var(--lime)}
  .cover__tagline{position:absolute;left:0;right:0;top:646px;text-align:center;font-size:16px;line-height:1.3}
  .panel--cover .web-band{background:var(--ink)}
  .panel--cover .web-tail{position:absolute;left:0;right:0;top:742px;bottom:0;background:var(--blue-deep)}
</style>
</head>
<body>
<main class="brochure">

  <section class="panel panel--about">
    <svg class="about__visual" viewBox="0 0 300 200" role="img" aria-label="Photo of a child drawing technology sketches on a wall, framed in a cloud shape">
      <defs>
        <linearGradient id="sketchTone" x1="0" y1="0" x2="1" y2="1">
          <stop offset="0" stop-color="#f2f2f2"/><stop offset="1" stop-color="#b9b9b9"/>
        </linearGradient>
      </defs>
      <path d="M40 170 C10 170 4 130 30 118 C18 90 50 66 78 78 C86 40 130 22 160 44 C178 10 236 14 244 56 C280 56 298 92 280 118 C300 136 288 172 256 172 Z" fill="url(#sketchTone)" stroke="#ffffff" stroke-width="5"/>
    </svg>
    <div class="about__heading"><h2>ABOUT US</h2></div>
    <div class="about__body">
      <p class="about__lead">K7 stands for Gather! Shape! Go!</p>
      <p>We are experts in 3D designing, scanning and printing technologies as well as Information Technology services.</p>
      <p>Our aim is to change the "consumer mentality" into "thinker/creator mentality".</p>
      <p>We hope to raise awareness about our planet's limited ressources and give companies and individuals the necessary tools to create a new world where we do not need to manage stocks, shipping or a" one size fits all" model.</p>
      <p>The two main activities of the company are software solutions development and training.</p>
      <p>We help companies build the information systems most suitable to their needs through understanding their business process.</p>
      <p>We act as your consultants to offer the best tools needed for your projects.</p>
      <p>Our goal is to offer a solution that is cost effective, maintainable and expandable.</p>
      <p>In some cases we would develop complete hardware/software solutions from scratch.</p>
      <p>Our clients vary from, Artists, Architects and Designers to Doctors, Teachers and even Cuisine gastronomique.</p>
    </div>
  </section>

  <section class="panel panel--contact">
    <div class="brandmark">
      <div class="brandmark__name">K7</div>
      <div class="brandmark__tag">GATHER! SHAPE! GO!</div>
    </div>
    <ul class="contact-list">
      <li>
        <svg width="14" height="14" viewBox="0 0 14 14"><rect x="0.5" y="0.5" width="13" height="13" rx="2" fill="#2a8ae0"/><path d="M4 3 L6 3 L6.5 5.5 L5.5 6.3 C6 7.6 6.6 8.2 7.7 8.7 L8.5 7.7 L11 8.2 L11 10 C7 10.5 3.6 7 4 3 Z" fill="#fff"/></svg>
        +4100 555 0172
      </li>
      <li>
        <svg width="16" height="12" viewBox="0 0 16 12"><rect x="0.5" y="0.5" width="15" height="11" rx="2" fill="#2a8ae0"/><path d="M2 2.5 L8 7 L14 2.5" stroke="#fff" stroke-width="1.4" fill="none"/></svg>
        Tarek@k7venturelab.example
      </li>
      <li class="contact--address">
        <svg width="14" height="14" viewBox="0 0 14 14"><rect x="0.5" y="0.5" width="13" height="13" rx="2" fill="#2a8ae0"/><path d="M3 7 L7 3.5 L11 7 L11 11 L3 11 Z" fill="#fff"/></svg>
        Rue des Lilas 8, Lakeview 4100 Switzerland
      </li>
    </ul>
    <div class="social" aria-label="Social media links">
      <span class="s1"></span><span class="s2"></span><span class="s3"></span><span class="s4"></span>
    </div>
    <div class="web-band">www.k7venturelab.example</div>
    <div class="web-tail"></div>
  </section>

  <section class="panel panel--cover">
    <div class="cover__photo" role="img" aria-label="Photo of a girl standing on a stack of books, looking over a brick wall at hot-air balloons in a sunset sky"></div>
    <div class="cover__rule"></div>
    <div class="cover__plate">
      <div class="brandmark__name">K7</div>
      <div class="brandmark__tag">GATHER! SHAPE! GO!</div>
    </div>
    <h1 class="cover__title">IMAGINATION</h1>
    <p class="cover__tagline">Should be used, not to escape reality<br>but to create it</p>
    <div class="web-band">www.k7venturelab.example</div>
    <div class="web-tail"></div>
  </section>

</main>
</body>
</html>
```